Golden Harbor Wealth
Golden Harbor Wealth Advisors, LLC
Golden Harbor Wealth - Financial Services
Creative Brief
Financial Services
Golden Harbor Wealth Advisors, LLC is a Michigan-based financial planning firm. We have comprehensive knowledge of strategies for Golden Harbor Wealth. At Golden Harbor Wealth Advisors we focus on helping retirees and those preparing for retirement to maximize their finances throughout their semi-retired and non-working years.
left side
Stonebridge Pension Group in Maryland
I want my website to model Stonebridge Pension Group in Maryland. I want similar language and I want those colors.
morvelin morvelin
Hi Designers, Logo Vector File uploaded. Thanks,
I am trying to get my logo posted. Thanks Dale

```html
<!DOCTYPE html>
<html lang="en">
<head>
<meta charset="utf-8">
<title>Golden Harbor Wealth Advisors</title>
<link href="https://fonts.googleapis.com/css2?family=Oswald:wght@400;500&family=Open+Sans:wght@400;600;700&family=Satisfy&display=swap" rel="stylesheet">
<style>
  :root {
    --green-dark: #0c5a30;
    --green: #137a40;
    --green-light: #1d9a52;
    --gold: #d9a521;
    --gold-light: #f0c84a;
    --page: #eceef1;
    --ink: #2f3438;
    --muted: #6b7075;
    --footer: #3a3d40;
    --caption: rgba(40, 40, 40, 0.78);
    --white: #ffffff;
  }
  * { box-sizing: border-box; margin: 0; padding: 0; }
  html, body { width: 1200px; height: 908px; overflow: hidden; }
  body { position: relative; background: var(--page); font-family: "Open Sans", Arial, sans-serif; color: var(--ink); }

  .header { position: absolute; left: 0; top: 0; width: 1200px; height: 461px; background: #f4f5f6; }
  .hero-photo {
    position: absolute; left: 540px; top: 74px; width: 660px; height: 387px;
    background: linear-gradient(120deg, #e9eef3 0%, #c9d6e2 40%, #a9bdd1 70%, #d8c3a6 100%);
  }
  .side-panel { position: absolute; left: 0; top: 0; width: 590px; height: 461px; }
  .logo-card { position: absolute; left: 0; top: 0; width: 590px; height: 461px; }
  .logo-name {
    position: absolute; left: 190px; top: 76px; width: 320px; text-align: center;
    font-family: "Open Sans", Arial, sans-serif; font-weight: 700; font-size: 22px; color: var(--green);
    line-height: 1.25;
  }
  .logo-mark { display: block; width: 18px; height: 18px; background: var(--gold); border-radius: 50%; margin: 0 auto 8px; }

  .nav { position: absolute; left: 142px; top: 200px; list-style: none; }
  .nav li { position: relative; height: 40px; width: 226px; padding-left: 42px; font-size: 15px; font-weight: 600; color: var(--white); line-height: 38px; }
  .nav li.active { background: linear-gradient(90deg, var(--gold), var(--gold-light)); clip-path: polygon(0 0, 100% 0, 92% 100%, 0 100%); color: var(--white); }

  .topbar-social { position: absolute; left: 852px; top: 26px; display: flex; gap: 8px; }
  .topbar-social span { width: 26px; height: 26px; border-radius: 50%; background: #b5b9bd; }
  .call { position: absolute; left: 950px; top: 22px; font-size: 12px; color: var(--green); }
  .call strong { display: flex; align-items: center; gap: 6px; margin-top: 3px; font-size: 17px; font-weight: 600; color: var(--ink); }

  .caption-band { position: absolute; left: 442px; top: 400px; width: 758px; height: 61px; background: var(--caption); }
  .welcome { position: absolute; left: 450px; top: 366px; font-family: "Satisfy", cursive; font-size: 30px; color: var(--white); text-shadow: 0 1px 2px rgba(0,0,0,.4); }
  .hero-title { position: absolute; left: 447px; top: 402px; font-family: "Oswald", sans-serif; font-size: 44px; color: var(--white); letter-spacing: 1px; line-height: 56px; }
  .hero-title em { font-family: "Satisfy", cursive; font-style: normal; font-size: 28px; color: var(--gold-light); margin-left: 6px; }
  .slider-dots { position: absolute; left: 1010px; top: 382px; display: flex; gap: 6px; }
  .slider-dots span { width: 13px; height: 13px; background: var(--gold); }
  .slider-dots span.on { background: var(--green-light); }

  .section-title {
    position: absolute; left: 471px; top: 496px; width: 314px; height: 50px;
    background: linear-gradient(90deg, var(--green-dark), var(--green-light));
    clip-path: polygon(6% 0, 100% 0, 94% 100%, 0 100%);
    border-right: 6px solid var(--gold);
    font-family: "Oswald", sans-serif; font-size: 30px; color: var(--white); text-align: center; line-height: 50px;
  }
  .title-accent { position: absolute; left: 775px; top: 496px; width: 12px; height: 50px; background: var(--gold); clip-path: polygon(70% 0, 100% 0, 30% 100%, 0 100%); }

  .service-thumb {
    position: absolute; width: 90px; height: 90px; transform: rotate(45deg);
    border: 5px solid var(--white); box-shadow: 0 3px 8px rgba(0,0,0,.25);
  }
  .service-name { position: absolute; font-size: 19px; color: var(--ink); letter-spacing: .5px; }
  .service-text { position: absolute; width: 200px; font-size: 11px; line-height: 15px; color: var(--muted); }
  .service-text b { color: var(--green); font-weight: 400; }
  .rule { position: absolute; height: 1px; background: #9aa09f; }
  .rule-dot { position: absolute; width: 11px; height: 11px; border-radius: 50%; background: var(--green); }

  .pager { position: absolute; left: 508px; top: 802px; width: 106px; height: 35px; background: var(--green); clip-path: polygon(12% 0, 100% 0, 88% 100%, 0 100%); display: flex; justify-content: center; align-items: center; gap: 18px; }

  .footer { position: absolute; left: 0; top: 859px; width: 1200px; height: 49px; background: var(--footer); color: #c4c7ca; font-size: 11px; text-align: center; line-height: 49px; }
</style>
</head>
<body>
  <header class="header">
    <div class="hero-photo" role="img" aria-label="Photo of a senior couple meeting with a financial advisor"></div>

    <svg class="side-panel" width="590" height="461" viewBox="0 0 590 461" aria-hidden="true">
      <defs>
        <linearGradient id="panelGreen" x1="0" y1="0" x2="1" y2="1">
          <stop offset="0" stop-color="#1a8c4a"/>
          <stop offset="1" stop-color="#0b5029"/>
        </linearGradient>
      </defs>
      <polygon points="0,0 560,0 430,461 0,461" fill="url(#panelGreen)"/>
      <polygon points="556,0 566,0 436,461 426,461" fill="#d9a521"/>
      <polygon points="215,30 540,30 490,160 147,160" fill="#ffffff"/>
    </svg>
    <div class="logo-name"><span class="logo-mark"></span>Golden Harbor Wealth</div>

    <ul class="nav">
      <li class="active">Home</li>
      <li>About Us</li>
      <li>Financial Services</li>
      <li>Clients</li>
      <li>Contact Us</li>
    </ul>

    <div class="topbar-social"><span></span><span></span></div>
    <div class="call">Call Us Today :
      <strong>
        <svg width="14" height="12" viewBox="0 0 14 12" aria-hidden="true"><rect width="14" height="12" rx="2" fill="#137a40"/><path d="M3 4c1 3 4 5 7 5l1-2-2-1-1 1C7 7 6 6 5 5l1-1-1-2z" fill="#fff"/></svg>
        555-018-274
      </strong>
    </div>

    <div class="caption-band"></div>
    <div class="welcome">Welcome to</div>
    <div class="hero-title">GOLDEN HARBOR<em>Wealth</em></div>
    <div class="slider-dots"><span class="on"></span><span></span><span></span></div>
  </header>

  <main class="services">
    <h2 class="section-title">OUR SERVICE</h2>
    <div class="title-accent"></div>

    <div class="service-thumb" style="left:232px;top:554px;background:linear-gradient(135deg,#f2f2f2,#8c8f92);" role="img" aria-label="Image of a pen resting on financial charts"></div>
    <div class="service-name" style="left:363px;top:568px;">INCOME PLANING</div>
    <div class="rule" style="left:363px;top:601px;width:557px;"></div>
    <div class="rule-dot" style="left:596px;top:596px;"></div>
    <div class="service-text" style="left:363px;top:618px;">Lorem ipsum dolor sit amet, consectetur adipiscing elit. Donec lectus augue, pulvinar imperdiet dolor at <b>[...]</b></div>
    <div class="service-name" style="left:633px;top:568px;">RETIREMENT PLANING</div>
    <div class="service-text" style="left:633px;top:618px;">Lorem ipsum dolor sit amet, consectetur adipiscing elit. Donec lectus augue, pulvinar imperdiet dolor at <b>[...]</b></div>
    <div class="service-thumb" style="left:956px;top:554px;background:linear-gradient(135deg,#e7dcc4,#6d5a3c);" role="img" aria-label="Image of coins and retirement savings"></div>

    <div class="service-thumb" style="left:142px;top:684px;background:linear-gradient(135deg,#b9a57a,#3e3a33);" role="img" aria-label="Image of stacked coins and money"></div>
    <div class="service-name" style="left:299px;top:690px;">FINANCIAL PLANING</div>
    <div class="rule" style="left:299px;top:724px;width:560px;"></div>
    <div class="rule-dot" style="left:564px;top:719px;"></div>
    <div class="service-text" style="left:299px;top:740px;">Lorem ipsum dolor sit amet, consectetur adipiscing elit. Donec lectus augue, pulvinar imperdiet dolor at <b>[...]</b></div>
    <div class="service-name" style="left:594px;top:690px;">EDUCATIONAL PLANING</div>
    <div class="service-text" style="left:594px;top:740px;">Lorem ipsum dolor sit amet, consectetur adipiscing elit. Donec lectus augue, pulvinar imperdiet dolor at <b>[...]</b></div>
    <div class="service-thumb" style="left:853px;top:676px;background:linear-gradient(135deg,#c8d6e4,#3d5670);" role="img" aria-label="Image of a graduate celebrating education"></div>

    <div class="pager" aria-label="Previous and next">
      <svg width="10" height="16" viewBox="0 0 10 16" aria-hidden="true"><path d="M8 1L2 8l6 7" fill="none" stroke="#fff" stroke-width="2"/></svg>
      <svg width="10" height="16" viewBox="0 0 10 16" aria-hidden="true"><path d="M2 1l6 7-6 7" fill="none" stroke="#fff" stroke-width="2"/></svg>
    </div>
  </main>

  <footer class="footer">©2015 Golden Harbor Wealth Advisors, LLC.com</footer>
</body>
</html>
```